Business Card design for an International Import Export House

We need a Business Card design for our import export business. We trade in Minerals, Metals, Rice, Sugar, Steel etc.. The design should be minimalistic. It may or may not contain the physical address. In case you want to include the physical address - 418 Verandah Heights, Marlow Sector 9, Kestrel Vale, Harlan, India, 410027.

Target Market(s)

Steel Mills or Steel Plants, Factories, Mining businesses, Industrial houses, Government Agencies

Industry/Entity Type

Importer

Contact Information for Business Card

Business Name - Tessan Overseas

Font styles to use
Other font styles liked:
• montserrat

Requirements
Must have
• Ravi Kandola - President
• www.tessanoverseas.com
• ravi@tessanoverseas.com
• +91-987-654-3217
Nice to have
• global traders of metals

```html
<!DOCTYPE html>
<html lang="en">
<head>
<meta charset="utf-8">
<title>Tessan Overseas – Business Card</title>
<link href="https://fonts.googleapis.com/css2?family=Montserrat:wght@700&family=Open+Sans:wght@400;600&display=swap" rel="stylesheet">
<style>
  :root {
    --teal: #4193ad;
    --teal-dark: #2f7f99;
    --ink: #1f2326;
    --text: #4a4d50;
    --rule: #d4d8da;
    --paper: #ffffff;
    --backdrop: #ececec;
  }
  * { box-sizing: border-box; margin: 0; padding: 0; }
  html, body {
    width: 1200px; height: 987px; overflow: hidden;
    background: var(--backdrop);
    font-family: "Open Sans", Arial, sans-serif;
  }
  .stage { position: relative; width: 1200px; height: 987px; }

  .card {
    position: absolute; left: 292px; width: 616px; height: 350px;
    box-shadow: 0 2px 6px rgba(0,0,0,.18);
    overflow: hidden;
  }
  .card--front { top: 130px; background: var(--paper); }
  .card--back { top: 505px; background: var(--teal); }

  .brand {
    position: absolute; display: flex; flex-direction: column; align-items: center;
  }
  .card--front .brand { left: 19px; width: 281px; top: 76px; }
  .card--back .brand { left: 0; width: 616px; top: 76px; }
  .brand__dot {
    width: 140px; height: 140px; border-radius: 50%;
    background: var(--teal);
  }
  .card--back .brand__dot { background: var(--paper); }
  .brand__name {
    margin-top: 28px;
    font-family: "Montserrat", Arial, sans-serif; font-weight: 700;
    font-size: 21px; letter-spacing: -0.3px; text-transform: uppercase;
    color: var(--ink); white-space: nowrap; line-height: 1.2;
  }
  .card--back .brand__name { color: var(--paper); font-size: 23px; margin-top: 30px; }

  .divider {
    position: absolute; left: 282px; top: 74px;
    width: 1px; height: 206px; background: var(--rule);
  }

  .details { position: absolute; left: 307px; top: 72px; color: var(--text); }
  .details__name {
    font-size: 21px; font-weight: 400; color: var(--teal);
    letter-spacing: 0.6px; text-transform: uppercase; line-height: 1.2;
  }
  .details__role { font-size: 16px; color: var(--ink); margin-top: 1px; line-height: 1.3; }
  .details__tagline { font-size: 15px; font-weight: 600; color: var(--ink); margin-top: 8px; line-height: 22px; }
  .details__address { font-size: 15px; line-height: 22px; }
  .contact { list-style: none; margin-top: 6px; }
  .contact__item {
    display: flex; align-items: center; gap: 9px;
    font-size: 15px; line-height: 23.5px;
  }
  .contact__icon { width: 14px; height: 14px; flex: none; fill: var(--teal-dark); }

  .band { position: absolute; left: 0; bottom: 0; height: 13px; width: 100%; display: flex; }
  .band__teal { width: 306px; background: linear-gradient(90deg, var(--teal-dark), var(--teal)); }
  .band__gap { width: 3px; background: var(--paper); }
  .band__ink { flex: 1; background: var(--ink); }
</style>
</head>
<body>
<main class="stage">

  <section class="card card--front" aria-label="Business card front">
    <div class="brand">
      <span class="brand__dot"></span>
      <span class="brand__name">Tessan Overseas</span>
    </div>
    <div class="divider"></div>
    <div class="details">
      <h1 class="details__name">Ravi Kandola</h1>
      <p class="details__role">President</p>
      <p class="details__tagline">global traders of metals</p>
      <p class="details__address">418 Verandah Heights, Marlow Sector 9<br>Kestrel Vale, Harlan, India, 410027.</p>
      <ul class="contact">
        <li class="contact__item">
          <svg class="contact__icon" viewBox="0 0 16 16" aria-hidden="true"><path d="M3.6 1.2 5.9 3.5c.4.4.4 1 0 1.4L4.7 6.1c.9 2 2.4 3.5 4.4 4.4l1.2-1.2c.4-.4 1-.4 1.4 0l2.3 2.3c.4.4.4 1 0 1.4l-1.3 1.3c-.6.6-1.6.8-2.4.4C6.6 13.2 2.8 9.4 1.3 5.7c-.4-.8-.2-1.8.4-2.4l1.3-1.3c.2-.3.4-.3.6-.3z"/></svg>
          +91-987-654-3217
        </li>
        <li class="contact__item">
          <svg class="contact__icon" viewBox="0 0 16 16" aria-hidden="true"><path d="M1 3h14v1.2L8 8.6 1 4.2z"/><path d="M1 5.6 8 10l7-4.4V13H1z"/></svg>
          ravi@tessanoverseas.com
        </li>
        <li class="contact__item">
          <svg class="contact__icon" viewBox="0 0 16 16" aria-hidden="true"><circle cx="8" cy="8" r="7"/><path d="M4 4.5c1.5 0 2 1 3 1.5s.5 2-1 2.2S5 10 5.5 12 3 10 2.5 8 3 4.5 4 4.5zM10 3c1 .5 1 1.5 2 1.5s1.5 2 1.5 3.5-1 1.5-2 1-2 .5-2.5 2-1-1-.5-2.5-1-2-.5-3S9 2.5 10 3z" fill="#fff"/></svg>
          www.tessanoverseas.com
        </li>
      </ul>
    </div>
    <div class="band">
      <span class="band__teal"></span><span class="band__gap"></span><span class="band__ink"></span>
    </div>
  </section>

  <section class="card card--back" aria-label="Business card back">
    <div class="brand">
      <span class="brand__dot"></span>
      <span class="brand__name">Tessan Overseas</span>
    </div>
  </section>

</main>
</body>
</html>
```